Eye catching business card

2 sided
Black background with logo in color on one side along with the words "Proudly serving the commercial and defense industries since 1975"
2nd side to contain contact information (see attached current business card) and "Waterjet, Composite, Precision Machining and Clean Room Manufacturing" with a very faint watermark of a waving USA Flag in the back ground.
Remove the "est. 195" from the current logo design

```html
<!DOCTYPE html>
<html lang="en">
<head>
<meta charset="utf-8">
<title>Northgate Fabrication – Business Card</title>
<link href="https://fonts.googleapis.com/css2?family=PT+Sans:wght@400;700&family=PT+Serif:ital,wght@1,700&family=Roboto:wght@400;700&display=swap" rel="stylesheet">
<style>
  :root {
    --stage: #2a2a2b;
    --card-dark: #231f20;
    --card-light: #ffffff;
    --accent-blue: #2a6fd1;
    --text-grey: #a7a7a9;
    --rule-grey: #8d8d8f;
    --brand-grey: #8a8b8d;
  }
  * { margin: 0; padding: 0; box-sizing: border-box; }
  html, body { width: 1200px; height: 1146px; overflow: hidden; }
  body { background: var(--stage); position: relative; font-family: "PT Sans", sans-serif; }

  .card {
    position: absolute;
    left: 260px;
    width: 680px;
    height: 440px;
    border-radius: 22px;
    overflow: hidden;
    background: var(--card-dark);
    box-shadow: 0 10px 30px rgba(0,0,0,.45);
  }
  .card--front { top: 90px; }
  .card--back { top: 606px; }

  /* Front */
  .front__top {
    position: absolute; left: 0; top: 0; width: 100%; height: 160px;
    background: var(--card-light);
    border-bottom: 3px solid var(--accent-blue);
    display: flex; align-items: center; justify-content: center;
  }
  .brand { display: flex; align-items: center; gap: 14px; color: var(--brand-grey); font-weight: 700; }
  .brand__mark { width: 40px; height: 40px; background: var(--accent-blue); border-radius: 4px; }
  .brand__name { display: flex; flex-direction: column; align-items: center; line-height: 1; }
  .brand__main { font-size: 36px; letter-spacing: 1px; }
  .brand__sub { font-size: 13px; letter-spacing: 6px; margin-top: 6px; }

  .front__tagline {
    position: absolute; left: 0; right: 0; top: 228px;
    text-align: center;
    font-family: "PT Serif", serif; font-style: italic; font-weight: 700;
    font-size: 29px; line-height: 1.45; letter-spacing: 1px;
    color: var(--text-grey);
  }

  /* Back */
  .back__shape { position: absolute; inset: 0; width: 100%; height: 100%; }
  .back__company { position: absolute; left: 77px; top: 48px; font-size: 31px; line-height: 40px; font-weight: 400; color: var(--text-grey); }
  .back__services { position: absolute; left: 77px; top: 102px; font-size: 20px; line-height: 36px; color: var(--text-grey); }
  .rule { position: absolute; left: 78px; width: 321px; height: 3px; background: var(--rule-grey); }
  .contact { position: absolute; left: 43px; height: 24px; display: flex; align-items: center; gap: 12px; font-size: 20px; line-height: 24px; color: var(--text-grey); white-space: nowrap; }
  .contact svg { width: 22px; height: 22px; flex: none; }

  .person { position: absolute; left: 470px; width: 196px; text-align: center; font-family: "Roboto", sans-serif; color: var(--accent-blue); white-space: nowrap; }
  .person__name { top: 156px; font-size: 28px; line-height: 34px; }
  .person__title { top: 191px; font-size: 22px; line-height: 26px; }
  .person__line { position: absolute; left: 445px; height: 22px; display: flex; align-items: center; gap: 6px; font-family: "Roboto", sans-serif; font-size: 17px; line-height: 22px; color: var(--accent-blue); white-space: nowrap; }
  .person__line b { font-weight: 700; }
  .person__line svg { width: 18px; height: 18px; flex: none; }
</style>
</head>
<body>

<section class="card card--front" aria-label="Card front">
  <div class="front__top">
    <div class="brand">
      <span class="brand__mark"></span>
      <span class="brand__name">
        <span class="brand__main">NORTHGATE</span>
        <span class="brand__sub">FABRICATION INC</span>
      </span>
    </div>
  </div>
  <p class="front__tagline">Proudly serving the commercial and<br>defense industries since 1975.</p>
</section>

<section class="card card--back" aria-label="Card back">
  <svg class="back__shape" viewBox="0 0 680 440" preserveAspectRatio="none" aria-hidden="true">
    <path d="M421,0 C455,50 482,95 478,140 C475,185 445,215 425,250 C405,285 398,320 402,360 C405,395 412,420 423,440 L680,440 L680,0 Z" fill="#ffffff"/>
    <path d="M421,0 C455,50 482,95 478,140 C475,185 445,215 425,250 C405,285 398,320 402,360 C405,395 412,420 423,440" fill="none" stroke="#2a6fd1" stroke-width="4"/>
  </svg>

  <h1 class="back__company">Northgate Fabrication, Inc.</h1>
  <p class="back__services">Waterjets, Composites, Precision<br>Machining and Clean Room Manufacturing.</p>

  <div class="rule" style="top:180px"></div>
  <div class="contact" style="top:192px">
    <svg viewBox="0 0 22 22"><rect x="1" y="1" width="20" height="20" rx="3" fill="none" stroke="#a7a7a9" stroke-width="1.5"/><path d="M6 11 L11 6.5 L16 11 V16 H12.5 V13 H9.5 V16 H6 Z" fill="#a7a7a9"/></svg>
    <span>412 Millbrook Rd. Glen Haven, PA 17000</span>
  </div>
  <div class="rule" style="top:228px"></div>
  <div class="contact" style="top:240px">
    <svg viewBox="0 0 22 22"><rect x="1" y="1" width="20" height="20" rx="3" fill="none" stroke="#a7a7a9" stroke-width="1.5"/><path d="M7 5 C6 6 6 9 8 12 C10 15 13 17 15 17 L16.5 15.5 L14 13.5 L12.5 14.5 C11 13.5 9.5 12 8.5 10 L9.5 8.5 L8 5.5 Z" fill="#a7a7a9"/></svg>
    <span>555-214-0008</span>
  </div>
  <div class="contact" style="top:277px">
    <svg viewBox="0 0 22 22"><rect x="1" y="1" width="20" height="20" rx="3" fill="none" stroke="#a7a7a9" stroke-width="1.5"/><rect x="7" y="5" width="8" height="4" fill="none" stroke="#a7a7a9" stroke-width="1.3"/><rect x="5" y="9" width="12" height="6" rx="1" fill="none" stroke="#a7a7a9" stroke-width="1.3"/><rect x="7.5" y="13" width="7" height="4" fill="none" stroke="#a7a7a9" stroke-width="1.3"/></svg>
    <span>Fax: 555-214-0040</span>
  </div>
  <div class="rule" style="top:312px"></div>
  <div class="contact" style="top:325px">
    <svg viewBox="0 0 22 22"><rect x="1" y="1" width="20" height="20" rx="3" fill="none" stroke="#a7a7a9" stroke-width="1.5"/><rect x="5" y="7" width="12" height="8" fill="none" stroke="#a7a7a9" stroke-width="1.3"/><path d="M5 7 L11 12 L17 7" fill="none" stroke="#a7a7a9" stroke-width="1.3"/></svg>
    <span>info@northgatefab.com</span>
  </div>
  <div class="contact" style="top:362px">
    <svg viewBox="0 0 22 22"><rect x="1" y="1" width="20" height="20" rx="3" fill="none" stroke="#a7a7a9" stroke-width="1.5"/><circle cx="11" cy="11" r="6" fill="none" stroke="#a7a7a9" stroke-width="1.2"/><ellipse cx="11" cy="11" rx="2.5" ry="6" fill="none" stroke="#a7a7a9" stroke-width="1"/><path d="M5 11 H17 M6 8 H16 M6 14 H16" stroke="#a7a7a9" stroke-width="1"/></svg>
    <span>www.northgatefab.com</span>
  </div>

  <p class="person person__name">Dale Hartman</p>
  <p class="person person__title">President</p>
  <div class="person__line" style="top:252px">
    <svg viewBox="0 0 18 18"><rect x="1" y="1" width="16" height="16" rx="3" fill="none" stroke="#2a6fd1" stroke-width="1.3"/><path d="M5.5 4 C4.8 5 4.8 7.5 6.5 10 C8 12.3 10.5 14 12 14 L13.3 12.8 L11.3 11.2 L10.2 12 C9 11.2 7.8 10 7 8.5 L7.8 7.3 L6.6 4.5 Z" fill="#2a6fd1"/></svg>
    <span>Office: <b>(555) 214-0008</b></span>
  </div>
  <div class="person__line" style="top:276px">
    <svg viewBox="0 0 18 18"><rect x="1" y="2" width="16" height="14" rx="3" fill="none" stroke="#2a6fd1" stroke-width="1.3"/><rect x="4" y="6" width="10" height="6.5" fill="none" stroke="#2a6fd1" stroke-width="1.1"/><path d="M4 6 L9 10 L14 6" fill="none" stroke="#2a6fd1" stroke-width="1.1"/></svg>
    <span>dale@northgatefab.com</span>
  </div>
</section>

</body>
</html>
```